The Perfect Business Card for PineHarbor

I am looking for a business card which beautifully incorporates my logo, reflects my business and looks special, elegant and clean.

```html
<!DOCTYPE html>
<html lang="en">
<head>
<meta charset="UTF-8">
<title>PineHarbor – Business Card</title>
<link rel="stylesheet" href="https://fonts.googleapis.com/css2?family=Roboto:wght@400;700&display=swap">
<style>
  :root {
    --card-bg: #ffffff;
    --brand-green: #6f9a3a;
    --accent-bar: #7aa23c;
    --name-ink: #4d4d4f;
    --body-ink: #333335;
  }
  html, body {
    margin: 0;
    padding: 0;
    width: 1200px;
    height: 686px;
    overflow: hidden;
    background: var(--card-bg);
  }
  .card {
    position: relative;
    width: 1200px;
    height: 686px;
    background: var(--card-bg);
    font-family: "Roboto", Arial, sans-serif;
    overflow: hidden;
  }
  .brand {
    position: absolute;
    left: 50px;
    top: 56px;
    display: flex;
    align-items: center;
  }
  .brand-ring {
    width: 204px;
    height: 204px;
    display: block;
  }
  .brand-name {
    margin-left: -40px;
    font-size: 64px;
    font-weight: 400;
    letter-spacing: 1px;
    color: var(--brand-green);
    line-height: 1;
  }
  .holder {
    position: absolute;
    left: 54px;
    top: 544px;
  }
  .holder-name {
    margin: 0;
    font-size: 46px;
    font-weight: 700;
    color: var(--name-ink);
    line-height: 46px;
  }
  .holder-role {
    margin: 6px 0 0;
    font-size: 26px;
    font-weight: 400;
    color: var(--body-ink);
    line-height: 30px;
  }
  .contact {
    position: absolute;
    left: 695px;
    top: 400px;
    margin: 0;
    padding: 0;
    list-style: none;
    font-size: 26px;
    color: var(--body-ink);
  }
  .contact li {
    line-height: 34px;
    margin-bottom: 20px;
  }
  .contact li.address {
    margin-bottom: 0;
    line-height: 38px;
  }
  .accent-bar {
    position: absolute;
    left: 1175px;
    top: 403px;
    width: 25px;
    height: 218px;
    background: var(--accent-bar);
  }
</style>
</head>
<body>
  <main class="card">
    <div class="brand">
      <svg class="brand-ring" viewBox="0 0 204 204" aria-hidden="true">
        <circle cx="102" cy="102" r="99" fill="none" stroke="var(--brand-green)" stroke-width="3"/>
      </svg>
      <span class="brand-name">PineHarbor</span>
    </div>

    <div class="holder">
      <h1 class="holder-name">Daniel Reyes</h1>
      <p class="holder-role">Manager – Business Development</p>
    </div>

    <ul class="contact">
      <li>email: daniel.reyes@pineharbor.ab</li>
      <li>mobile: +00-987654321</li>
      <li>www.pineharbor.com</li>
      <li class="address">address: Myrtle 42 Str. 15671,<br>Halcyon, Athens, Greece</li>
    </ul>

    <div class="accent-bar"></div>
  </main>
</body>
</html>
```